RV park billboard

We need a billboard for cedar bend RV park . I was thinking about having a big orange in the background. We will have free fiber optic internet and each camper will have its own personal hotspot and we want that on the sign... Also the phone number with the area code... But I don't have the exact number yet. Size of sign will be 12 x 40
Updates
Make sure sign has Cedar Bend RV park on it
Target Market(s)
Plant turnaround workers
Look and feel

```html
<!DOCTYPE html>
<html lang="en">
<head>
<meta charset="UTF-8">
<title>Cedar Bend RV Park – Billboard</title>
<link rel="stylesheet" href="https://fonts.googleapis.com/css2?family=Bebas+Neue&family=Oswald:wght@600&display=swap">
<style>
  :root {
    --page-bg: #e9ecef;
    --sky-amber: #c98a2a;
    --burnt-orange: #d9641c;
    --earth-brown: #5b3614;
    --fruit-area: #e9742a;
    --text-white: #ffffff;
    --tick-orange: #f5a030;
    --call-start: #f07a22;
    --call-end: #fbbd3c;
  }
  * { margin: 0; padding: 0; box-sizing: border-box; }
  html, body {
    width: 1200px;
    height: 840px;
    overflow: hidden;
    background: var(--page-bg);
  }
  .canvas {
    position: relative;
    width: 1200px;
    height: 840px;
    display: flex;
    align-items: center;
    justify-content: center;
  }
  .billboard {
    position: relative;
    width: 1120px;
    height: 336px;
    overflow: hidden;
  }
  .scene-photo {
    position: absolute;
    inset: 0;
    background:
      linear-gradient(180deg, rgba(0,0,0,0) 55%, rgba(70,40,10,0.55) 100%),
      radial-gradient(ellipse 40% 55% at 55% 35%, var(--earth-brown) 0%, rgba(91,54,20,0) 70%),
      linear-gradient(90deg, var(--sky-amber) 0%, #b9702a 35%, var(--burnt-orange) 75%, #c4541a 100%);
  }
  .fruit-art {
    position: absolute;
    left: 8px;
    top: 10px;
    width: 268px;
    height: 290px;
    background: var(--fruit-area);
  }
  .brand-name {
    position: absolute;
    left: 292px;
    top: 48px;
    font-family: "Bebas Neue", sans-serif;
    font-weight: 400;
    color: var(--text-white);
    font-size: 118px;
    line-height: 0.95;
    letter-spacing: 2px;
  }
  .features {
    position: absolute;
    left: 812px;
    top: 44px;
    width: 290px;
    list-style: none;
    font-family: "Oswald", sans-serif;
    font-weight: 600;
    color: var(--text-white);
    font-size: 27px;
    line-height: 1.15;
    text-transform: uppercase;
  }
  .feature {
    display: flex;
    align-items: flex-start;
    gap: 8px;
    margin-bottom: 10px;
  }
  .feature svg { flex: none; margin-top: 2px; }
  .call-button {
    position: absolute;
    left: 804px;
    top: 206px;
    width: 306px;
    height: 64px;
    border-radius: 12px;
    background: linear-gradient(90deg, var(--call-start), var(--call-end));
    display: flex;
    align-items: center;
    justify-content: center;
    font-family: "Oswald", sans-serif;
    font-weight: 600;
    font-size: 30px;
    color: var(--text-white);
    letter-spacing: 0.5px;
  }
</style>
</head>
<body>
<main class="canvas">
  <section class="billboard">
    <div class="scene-photo" role="img" aria-label="Photograph of a motorhome parked on a road beside mountains and grassland with a welcome signpost, tinted warm orange"></div>

    <div class="fruit-art" role="img" aria-label="Illustration of a large orange fruit with a green leaf"></div>

    <h1 class="brand-name">Cedar Bend<br>RV Park</h1>

    <ul class="features">
      <li class="feature">
        <svg width="30" height="30" viewBox="0 0 30 30" aria-hidden="true"><path d="M3 16 L12 25 L27 4" fill="none" stroke="var(--tick-orange)" stroke-width="5" stroke-linecap="round" stroke-linejoin="round"/></svg>
        <span>Free fiber<br>optic internet</span>
      </li>
      <li class="feature">
        <svg width="30" height="30" viewBox="0 0 30 30" aria-hidden="true"><path d="M3 16 L12 25 L27 4" fill="none" stroke="var(--tick-orange)" stroke-width="5" stroke-linecap="round" stroke-linejoin="round"/></svg>
        <span>Personal hotspot</span>
      </li>
    </ul>

    <div class="call-button">CALL (409) 555-0142</div>
  </section>
</main>
</body>
</html>
```